Dentist Home Page Design

We need a home page design to be used as a responsive wordpress theme for our dentist website. Website overall look and feel should look professional, yet very friendly as going to dentist is not people's favorite thing to do, for most it might even be scary. We want our website to differentiate with its design from all other generic looking cookie cutter dentists and creates a branded feel.
you can use a generic image for the 680x300px banner on the home pageif you like in the meantime). Total width should not exceed 960 px
Please follow the layout on the wireframes, do not add or delete random elements.
Target Market(s)
mostly targets male/female between 30-45, families with kids as well.
Industry/Entity Type
It Professional
Colors
Designer to choose colors to be used in the design.
Look and feel
Each slider illustrates characteristics of the customer's brand and the style your logo design should communicate.

```html
<!DOCTYPE html>
<html lang="en">
<head>
<meta charset="utf-8">
<title>Brightside Dental – Home</title>
<link href="https://fonts.googleapis.com/css2?family=Barlow:wght@500;600;700&family=Didact+Gothic&display=swap" rel="stylesheet">
<style>
  :root {
    --white: #ffffff;
    --ink: #2e2e2e;
    --brand-navy: #1f3f8f;
    --accent-red: #ef2637;
    --accent-red-line: #f45a66;
    --hero-light: #e9eef2;
    --hero-mid: #c9d3dc;
    --hero-blue: #6f9fd0;
  }
  * { margin: 0; padding: 0; box-sizing: border-box; }
  html, body { width: 1200px; height: 607px; overflow: hidden; background: var(--white); }
  body { position: relative; font-family: "Didact Gothic", sans-serif; }

  .site-header { position: absolute; left: 0; top: 0; width: 1200px; height: 98px; background: var(--white); }
  .brand {
    position: absolute; left: 185px; top: 36px;
    display: flex; align-items: center; gap: 10px;
    font-family: "Barlow", sans-serif; font-weight: 700; font-size: 22px;
    color: var(--brand-navy); letter-spacing: 0.3px;
  }
  .brand-dot { width: 14px; height: 14px; border-radius: 50%; background: var(--accent-red); }

  .main-nav { position: absolute; left: 410px; top: 41px; display: flex; }
  .main-nav a {
    font-size: 11.5px; letter-spacing: 0.9px; text-transform: uppercase;
    color: var(--ink); text-decoration: none; margin-right: 13px; white-space: nowrap;
  }
  .main-nav a.contact { margin-left: 7px; margin-right: 0; }

  .hero { position: absolute; left: 0; top: 98px; width: 1200px; height: 480px; overflow: hidden; }
  .hero-photo {
    position: absolute; inset: 0;
    background:
      radial-gradient(ellipse 320px 260px at 420px 360px, var(--hero-blue) 0%, rgba(111,159,208,0) 100%),
      radial-gradient(ellipse 260px 140px at 170px 80px, #8aa8bd 0%, rgba(138,168,189,0) 100%),
      linear-gradient(90deg, var(--hero-mid) 0%, var(--hero-light) 45%, #f4f6f7 75%, var(--hero-mid) 100%);
  }
  .hero-title {
    position: absolute; left: 0; top: 140px; width: 1200px; text-align: center;
    font-family: "Barlow", sans-serif; color: var(--white); text-transform: uppercase;
    text-shadow: 0 2px 8px rgba(0,0,0,0.25);
  }
  .hero-title .line-one { display: block; font-weight: 600; font-size: 54px; letter-spacing: 4px; line-height: 58px; }
  .hero-title .line-two { display: block; font-weight: 700; font-size: 78px; letter-spacing: 4px; line-height: 80px; }

  .hero-cta {
    position: absolute; left: 394px; top: 296px; width: 412px; height: 49px;
    background: var(--accent-red); display: flex; text-decoration: none;
  }
  .hero-cta-label {
    width: 349px; display: flex; align-items: center; padding-left: 17px;
    font-family: "Barlow", sans-serif; font-weight: 700; font-size: 13.5px;
    letter-spacing: 3.2px; color: var(--white); text-transform: uppercase;
    border-right: 1px solid var(--accent-red-line);
  }
  .hero-cta-icon { flex: 1; display: flex; align-items: center; justify-content: center; }
</style>
</head>
<body>
  <header class="site-header">
    <div class="brand"><span class="brand-dot"></span>Brightside Dental</div>
    <nav class="main-nav">
      <a href="#">Home</a>
      <a href="#">About</a>
      <a href="#">Services</a>
      <a href="#">Technology</a>
      <a href="#">Dental Care</a>
      <a href="#">Case Studies</a>
      <a href="#">New Patients</a>
      <a href="#" class="contact">Contact</a>
    </nav>
  </header>

  <section class="hero">
    <div class="hero-photo" role="img" aria-label="Photo of a smiling dentist in a blue shirt and mask at a treatment chair with a patient, in a bright modern clinic"></div>
    <h1 class="hero-title">
      <span class="line-one">Your experience in dentistry</span>
      <span class="line-two">begins now!</span>
    </h1>
    <a class="hero-cta" href="#">
      <span class="hero-cta-label">Find out more about our work</span>
      <span class="hero-cta-icon">
        <svg width="12" height="13" viewBox="0 0 12 13" aria-hidden="true"><path d="M1 0.5 L11 6.5 L1 12.5 Z" fill="#ffffff"/></svg>
      </span>
    </a>
  </section>
</body>
</html>
```